Hadley & Partners, LLC Business Card 2016

We need a new business card design for a very important trade show coming up.

We are a compliance Consulting Firm. Our clients are stock brokerage firms and investment advisers.

I would like our logo on both sides of the card.

Info in the front of the card shold include:

Logo
First & Last Name
Title
Office #
Cell #
Email
Company Address (42 W. Calloway St., Suite 300 Pasadena, CA 91417

Back of the card should include the logo and url: www.hadleypartnersgroup.com

Target Market(s)

Stock Brokerage Firms and Investment Advisers

Industry/Entity Type

Financial Service

Contact Information for Business Card

Marcus J. Pellew
President
42 W. Calloway St., Suite 300
Pasadena, CA 91417
O 626.555.0147 ext. 204
C 818.555.0193
Email: marcus@hadleypartnersgroup.com
www.hadleypartnersgroup.com

Requirements
Nice to have
• The back of the card could be black with the logo with the white letters.
• I do want the front of the card to at least have the color logo with the black "Hadley & Partners Lettering.

```html
<!DOCTYPE html>
<html lang="en">
<head>
<meta charset="utf-8">
<title>Hadley &amp; Partners — Business Card</title>
<link rel="stylesheet" href="https://fonts.googleapis.com/css2?family=Cinzel:wght@600&family=Lato:wght@400&display=swap">
<style>
  :root {
    --page: #e4e4e4;
    --card-white: #ffffff;
    --card-black: #000000;
    --brand-red: #b8231f;
    --icon-red: #e8141c;
    --name-pink: #e8475a;
    --title-gray: #6a6a6a;
    --band-dark: #575c61;
    --band-light: #8a8f94;
    --text-white: #ffffff;
    --ink: #141414;
  }
  * { margin: 0; padding: 0; box-sizing: border-box; }
  html, body {
    width: 1200px; height: 1200px; overflow: hidden;
    background: var(--page);
  }
  .card {
    position: absolute; left: 192px; width: 816px; height: 468px;
    overflow: hidden; box-shadow: 0 14px 24px rgba(0,0,0,0.25);
  }
  .card--front { top: 60px; background: var(--card-black); }
  .card--back { top: 640px; background: var(--card-black); }

  .front__top {
    position: absolute; left: 0; top: 0; width: 100%; height: 233px;
    background: var(--card-white);
  }
  .holder__name {
    position: absolute; left: 11px; top: 4px;
    font: 400 31px/1.1 "Lato", sans-serif; color: var(--name-pink);
  }
  .holder__title {
    position: absolute; left: 13px; top: 38px;
    font: 400 17px/1.1 "Lato", sans-serif; color: var(--title-gray);
  }
  .wordmark {
    position: absolute; left: 0; width: 100%; text-align: center;
    font: 600 46px/1 "Cinzel", serif; letter-spacing: 1px; white-space: nowrap;
  }
  .wordmark--front { top: 150px; color: var(--ink); }
  .wordmark--back { top: 215px; color: var(--text-white); }

  .contact {
    position: absolute; color: var(--text-white);
    font: 400 14.5px/1.35 "Lato", sans-serif; white-space: nowrap;
  }
  .contact--phones { left: 49px; top: 290px; }
  .contact--email { right: 232px; top: 302px; }
  .contact--web { left: 10px; top: 359px; }
  .contact--address { left: 357px; top: 347px; font-size: 15.5px; }

  .icon { position: absolute; width: 36px; height: 36px; }
  .icon--phone { left: 265px; top: 294px; }
  .icon--email { left: 598px; top: 293px; }
  .icon--web { left: 265px; top: 350px; }
  .icon--pin { left: 598px; top: 350px; }

  .front__stripe { position: absolute; top: 451px; height: 17px; }
  .front__stripe--red { left: 0; width: 599px; background: var(--brand-red); }
  .front__stripe--dark { left: 599px; width: 126px; background: var(--band-dark); }
  .front__stripe--light { left: 725px; width: 91px; background: var(--band-light); }

  .back__band {
    position: absolute; left: 0; top: 424px; width: 100%; height: 44px;
    background: var(--band-dark);
  }
  .back__tab { position: absolute; left: 0; top: 407px; width: 816px; height: 61px; }
  .back__url {
    position: absolute; left: 0; top: 421px; width: 100%; text-align: center;
    font: 400 20px/1.2 "Lato", sans-serif; color: var(--text-white);
  }
</style>
</head>
<body>

<section class="card card--front" aria-label="Card front">
  <div class="front__top"></div>
  <p class="holder__name">Marcus J. Pellew</p>
  <p class="holder__title">President</p>
  <p class="wordmark wordmark--front">HADLEY &amp; PARTNERS</p>

  <p class="contact contact--phones">O : 626.555.0147 ext. : 204<br>C : 818.555.0193</p>
  <svg class="icon icon--phone" viewBox="0 0 36 36" aria-hidden="true">
    <circle cx="18" cy="18" r="18" fill="var(--icon-red)"/>
    <path d="M12 10c1-1 2-1 3 0l2 3c.5 1 0 2-1 2.5l-.8.5c.8 2 2.5 3.8 4.5 4.6l.5-.8c.6-1 1.6-1.4 2.5-.9l3 2c1 .7 1 1.8 0 2.8l-1.5 1.3c-5 1.2-14-7.8-12.8-12.8z" fill="#fff"/>
  </svg>

  <p class="contact contact--email">marcus@hadleypartnersgroup.com</p>
  <svg class="icon icon--email" viewBox="0 0 36 36" aria-hidden="true">
    <circle cx="18" cy="18" r="18" fill="var(--icon-red)"/>
    <rect x="10" y="12.5" width="16" height="11" fill="#fff"/>
    <path d="M10 12.5l8 6 8-6M10 23.5l6-5M26 23.5l-6-5" stroke="var(--icon-red)" stroke-width="1.4" fill="none"/>
  </svg>

  <p class="contact contact--web">www.hadleypartnersgroup.com</p>
  <svg class="icon icon--web" viewBox="0 0 36 36" aria-hidden="true">
    <circle cx="18" cy="18" r="18" fill="var(--icon-red)"/>
    <circle cx="18" cy="18" r="10" fill="none" stroke="#fff" stroke-width="1.8"/>
    <ellipse cx="18" cy="18" rx="4.5" ry="10" fill="none" stroke="#fff" stroke-width="1.6"/>
    <path d="M8 18h20M10 13h16M10 23h16" stroke="#fff" stroke-width="1.4"/>
  </svg>

  <p class="contact contact--address">42 W. Calloway St., Suite 300<br>Pasadena, CA 91417</p>
  <svg class="icon icon--pin" viewBox="0 0 36 36" aria-hidden="true">
    <circle cx="18" cy="18" r="18" fill="var(--icon-red)"/>
    <path d="M18 8a6 6 0 0 1 6 6c0 4.5-6 12-6 12s-6-7.5-6-12a6 6 0 0 1 6-6z" fill="#fff"/>
    <circle cx="18" cy="14" r="2.2" fill="var(--icon-red)"/>
  </svg>

  <div class="front__stripe front__stripe--red"></div>
  <div class="front__stripe front__stripe--dark"></div>
  <div class="front__stripe front__stripe--light"></div>
</section>

<section class="card card--back" aria-label="Card back">
  <p class="wordmark wordmark--back">HADLEY &amp; PARTNERS</p>
  <div class="back__band"></div>
  <svg class="back__tab" viewBox="0 0 816 61" aria-hidden="true">
    <polygon points="250,0 565,0 575,61 237,61" fill="var(--brand-red)"/>
  </svg>
  <p class="back__url">www.hadleypartnersgroup.com</p>
</section>

</body>
</html>
```